FotoVELTA buisnesscard

Hey :) I need a modern buisnesscard for my company FotoVELTA
It most have:
Dagligleder og Fotograf: Henrik Torvald Bjelland

Mob: +4791642058
Epost: post@fotovelta.no
Adresse: Bakkestien22, 5871 Fjordvik

Facbook and instagram logo with text FotoVELTA

FotoVELTA logo

It Company

```html
<!DOCTYPE html>
<html lang="no">
<head>
<meta charset="utf-8">
<title>FotoVELTA – visittkort</title>
<link rel="stylesheet" href="https://fonts.googleapis.com/css2?family=Noto+Sans:wght@400;700&display=swap">
<style>
  :root {
    --page: #eceae7;
    --blue: #2f8dbd;
    --blue-deep: #2a80b2;
    --blue-light: #3a9bc9;
    --line: #2f86bb;
    --paper: #fdf9f9;
    --pink: #c9508f;
    --white: #ffffff;
  }
  * { box-sizing: border-box; margin: 0; padding: 0; }
  html, body {
    width: 1200px; height: 1200px; overflow: hidden;
    background: var(--page);
    font-family: "Noto Sans", Verdana, sans-serif;
  }
  .sheet {
    width: 1200px; height: 1200px;
    display: flex; flex-direction: column; align-items: center;
    justify-content: center; gap: 84px;
  }
  .card {
    position: relative;
    width: 720px; height: 436px;
    background: linear-gradient(160deg, var(--blue-light), var(--blue) 50%, var(--blue-deep));
  }
  .card__face {
    position: absolute; top: 24px; left: 24px; right: 21px; height: 342px;
    background: var(--paper);
    display: flex; flex-direction: column; align-items: center; justify-content: center;
  }
  .bracket {
    position: absolute; width: 40px; height: 40px;
    border-color: var(--line); border-style: solid; border-width: 0;
  }
  .bracket--tl { top: 15px; left: 15px; border-top-width: 2px; border-left-width: 2px; }
  .bracket--tr { top: 15px; right: 15px; border-top-width: 2px; border-right-width: 2px; }
  .bracket--bl { bottom: 18px; left: 15px; border-bottom-width: 2px; border-left-width: 2px; }
  .bracket--br { bottom: 18px; right: 15px; border-bottom-width: 2px; border-right-width: 2px; }

  .person__name { color: var(--blue); font-size: 27px; font-weight: 400; letter-spacing: 0.3px; }
  .person__ring { margin: 8px 0 4px; }
  .person__role { color: var(--pink); font-size: 17.5px; }

  .card__footer {
    position: absolute; left: 0; right: 0; bottom: 0; height: 70px;
    display: flex; flex-direction: column; align-items: center; justify-content: center;
    color: var(--white); font-size: 17.5px; line-height: 22px; letter-spacing: 0.2px;
  }
  .card__footer--social { flex-direction: row; gap: 22px; font-size: 19.5px; }
  .social { display: flex; align-items: center; gap: 12px; }
  .social__dot {
    width: 33px; height: 33px; border-radius: 50%;
    border: 1.5px solid var(--white);
  }

  .brand { display: flex; align-items: center; gap: 14px; }
  .brand__square { width: 34px; height: 34px; background: var(--pink); }
  .brand__name { color: var(--blue); font-size: 52px; font-weight: 700; letter-spacing: -0.5px; }
</style>
</head>
<body>
<main class="sheet">
  <section class="card card--front">
    <div class="card__face">
      <span class="bracket bracket--tl"></span><span class="bracket bracket--tr"></span>
      <span class="bracket bracket--bl"></span><span class="bracket bracket--br"></span>
      <h1 class="person__name">Henrik Torvald Bjelland</h1>
      <svg class="person__ring" width="18" height="18" viewBox="0 0 18 18" aria-hidden="true">
        <circle cx="9" cy="9" r="8" fill="none" stroke="var(--blue)" stroke-width="1.3"/>
        <circle cx="9" cy="9" r="4.5" fill="none" stroke="var(--blue)" stroke-width="1.3"/>
      </svg>
      <p class="person__role">Dagligleder og Fotograf</p>
    </div>
    <footer class="card__footer">
      <p>M: 491 642 058 | www.fotovelta.no | post@fotovelta.no</p>
      <p>Bakkestien22, 5871 Fjordvik</p>
    </footer>
  </section>

  <section class="card card--back">
    <div class="card__face">
      <span class="bracket bracket--tl"></span><span class="bracket bracket--tr"></span>
      <span class="bracket bracket--bl"></span><span class="bracket bracket--br"></span>
      <div class="brand">
        <span class="brand__square" aria-hidden="true"></span>
        <span class="brand__name">FotoVELTA</span>
      </div>
    </div>
    <footer class="card__footer card__footer--social">
      <span class="social"><span class="social__dot" aria-hidden="true"></span>FotoVELTA</span>
      <span class="social"><span class="social__dot" aria-hidden="true"></span>FotoVELTA</span>
    </footer>
  </section>
</main>
</body>
</html>
```